Labels designs for a new coffee brand (Velloru Coffee)

We looking for a coffee label design for our coffee Brand, VELLORU COFFE, attached is the logo. We are bringing out to the market 3 Premium blends
1. Colombian Popayan
2. Gourmet Expresso Blend
3. Brazilian Santos

We like something that looks high quality yet modern, the bags we are using is black matte, we are starting with labels and look in the near future to print our own labels .

We want the labels for the 3 coffees to have the similar look and feel but to be uniquely identified by its design (Colombian, Brazilian, espresso) This is beig sold as a set so we want it to have a similar label feeling but that each is identify as its unique product (colombian, expresso, brazilian blend.

This project is for labels that will be used on a black matte bag, is for a 16 oz bag,

Attached is a sample of the bag color.

Size Requirements:
Maintain a 2:3 aspect ratio for the image file
The label will be 4" wide and 6" tall (we also want to print some 3X4)
Recommended image size is 1600px X 2400px

I will provide upc later

www.vellorucoffee.example pw 12345 this is the test site not live yet but you can get a feel of the brand

Ay my daughters volleyball tournament I need extra time to review

coffee drinkers

coffee

• Creativity, unique, eye catchy,

```html
<!DOCTYPE html>
<html lang="en">
<head>
<meta charset="utf-8">
<title>Velloru Coffee — Premium Blend Labels</title>
<link rel="stylesheet" href="https://fonts.googleapis.com/css2?family=Baloo+2:wght@700;800&family=Montserrat:wght@400;600;700&display=swap">
<style>
  :root {
    --backdrop: #cbcbcb;
    --navy: #0d1a33;
    --navy-line: #1c2a47;
    --teal: #12a58a;
    --orange: #fb4f06;
    --crimson: #cf0c3c;
    --paper: #e4e1bf;
    --paper-edge: #f3f0dc;
    --ink: #111111;
    --white: #ffffff;
  }
  * { box-sizing: border-box; margin: 0; padding: 0; }
  html, body { width: 1200px; height: 873px; overflow: hidden; }
  body {
    background: var(--backdrop);
    font-family: "Montserrat", sans-serif;
    display: flex;
    align-items: center;
    justify-content: center;
    gap: 80px;
  }
  .bag {
    width: 250px;
    height: 620px;
    display: flex;
    flex-direction: column;
    box-shadow: 0 6px 18px rgba(0,0,0,0.12);
  }
  .bag__brand {
    flex: 0 0 58%;
    background: var(--navy);
    color: var(--white);
    display: flex;
    flex-direction: column;
    align-items: center;
    padding-top: 90px;
    text-align: center;
  }
  .tagline {
    font-weight: 700;
    font-size: 9px;
    letter-spacing: 2px;
  }
  .tagline__place {
    font-weight: 600;
    font-size: 5.5px;
    letter-spacing: 1px;
    margin-top: 3px;
  }
  .brand-mark {
    width: 64px;
    height: 64px;
    border: 4px solid var(--white);
    border-radius: 50%;
    margin-top: 95px;
  }
  .brand-name {
    font-weight: 700;
    font-size: 17px;
    letter-spacing: 1px;
    margin-top: 26px;
  }
  .bag__product {
    flex: 1;
    display: flex;
    flex-direction: column;
    align-items: center;
    padding: 22px 14px 0;
  }
  .bag--espresso .bag__product { background: var(--teal); }
  .bag--brazil .bag__product { background: var(--orange); }
  .bag--colombia .bag__product { background: var(--crimson); }
  .product-name {
    font-family: "Baloo 2", sans-serif;
    font-weight: 800;
    font-size: 24px;
    line-height: 1;
    color: var(--white);
    text-align: center;
    height: 54px;
    display: flex;
    align-items: center;
  }
  .bag--espresso .product-name { font-size: 19px; }
  .spec-card {
    margin-top: 10px;
    width: 100%;
    background: var(--paper-edge);
    padding: 7px;
    border: 2px dashed var(--paper-edge);
  }
  .spec-card__inner {
    background: var(--paper);
    padding: 14px 12px 10px;
    color: var(--ink);
  }
  .spec-card__origin {
    font-weight: 700;
    font-size: 11px;
  }
  .spec-card__notes {
    font-size: 5.5px;
    padding-bottom: 3px;
    border-bottom: 1px solid var(--ink);
  }
  .spec-card__grid {
    display: grid;
    grid-template-columns: 1fr 1fr;
    height: 58px;
  }
  .spec-card__cell {
    display: flex;
    flex-direction: column;
    justify-content: center;
    align-items: center;
    text-align: center;
  }
  .spec-card__cell + .spec-card__cell { border-left: 1px solid var(--ink); }
  .spec-strong { font-weight: 700; font-size: 10px; }
  .spec-light { font-size: 8px; }
</style>
</head>
<body>

<article class="bag bag--espresso">
  <header class="bag__brand">
    <p class="tagline">SMALL-BATCH ROASTED</p>
    <p class="tagline__place">TACOMA, WA</p>
    <span class="brand-mark" aria-hidden="true"></span>
    <p class="brand-name">VELLORU COFFEE</p>
  </header>
  <section class="bag__product">
    <h2 class="product-name">Gourmet Expresso<br>Blend</h2>
    <div class="spec-card">
      <div class="spec-card__inner">
        <p class="spec-card__origin">Colombia</p>
        <p class="spec-card__notes">Notes of dark brown sugar, gianduja, cream</p>
        <div class="spec-card__grid">
          <div class="spec-card__cell"><span class="spec-strong">Whole Beam</span><span class="spec-light">Coffee</span></div>
          <div class="spec-card__cell"><span class="spec-strong">12 Oz</span><span class="spec-light">340 gr</span></div>
        </div>
      </div>
    </div>
  </section>
</article>

<article class="bag bag--brazil">
  <header class="bag__brand">
    <p class="tagline">SMALL-BATCH ROASTED</p>
    <p class="tagline__place">TACOMA, WA</p>
    <span class="brand-mark" aria-hidden="true"></span>
    <p class="brand-name">VELLORU COFFEE</p>
  </header>
  <section class="bag__product">
    <h2 class="product-name">Brazilian<br>Santos</h2>
    <div class="spec-card">
      <div class="spec-card__inner">
        <p class="spec-card__origin">Colombia</p>
        <p class="spec-card__notes">Notes of dark brown sugar, gianduja, cream</p>
        <div class="spec-card__grid">
          <div class="spec-card__cell"><span class="spec-strong">Whole Beam</span><span class="spec-light">Coffee</span></div>
          <div class="spec-card__cell"><span class="spec-strong">12 Oz</span><span class="spec-light">340 gr</span></div>
        </div>
      </div>
    </div>
  </section>
</article>

<article class="bag bag--colombia">
  <header class="bag__brand">
    <p class="tagline">SMALL-BATCH ROASTED</p>
    <p class="tagline__place">TACOMA, WA</p>
    <span class="brand-mark" aria-hidden="true"></span>
    <p class="brand-name">VELLORU COFFEE</p>
  </header>
  <section class="bag__product">
    <h2 class="product-name">Colombian<br>Popayan</h2>
    <div class="spec-card">
      <div class="spec-card__inner">
        <p class="spec-card__origin">Colombia</p>
        <p class="spec-card__notes">Notes of dark brown sugar, gianduja, cream</p>
        <div class="spec-card__grid">
          <div class="spec-card__cell"><span class="spec-strong">Whole Beam</span><span class="spec-light">Coffee</span></div>
          <div class="spec-card__cell"><span class="spec-strong">12 Oz</span><span class="spec-light">340 gr</span></div>
        </div>
      </div>
    </div>
  </section>
</article>

</body>
</html>
```